Talbix Pens needs a new Webpage for their collection of ballpens

We at Talbix pens need a brand new webpage to represent our company and range of products. We need a product based website to focus purely on our collection. The web design must bring about a perception of high quality International brand but still affordable in price. Since there are only 5 products, they must all feature on the cover page itself.

Target Market(s)

Stationary Wholesale and retail

Industry/Entity Type

It Company

Number of Pages Required

1 page

Requirements
Must have
• pls see www.quendora-example.com to derive inspiration
Should not have
• stock images
• abstract images
• random pen images

```html
<!DOCTYPE html>
<html lang="en">
<head>
<meta charset="utf-8">
<title>Talbix Pens</title>
<link href="https://fonts.googleapis.com/css2?family=Open+Sans:wght@300;400;600;700&family=Oswald:wght@200&display=swap" rel="stylesheet">
<style>
:root{
  --blue:#1766a2;
  --royal:#0a2fa0;
  --ink:#1d1d1d;
  --red:#ff0a0a;
  --paper:#f4f4f4;
  --grid:#ececec;
  --grey:#6b6b6b;
  --violet:#4a2aa6;
}
*{margin:0;padding:0;box-sizing:border-box}
html,body{width:757px;height:1200px;overflow:hidden}
body{position:relative;font-family:"Open Sans",sans-serif;color:var(--ink);
  background-color:var(--paper);
  background-image:linear-gradient(var(--grid) 1px,transparent 1px),linear-gradient(90deg,var(--grid) 1px,transparent 1px);
  background-size:12px 12px}
.brand-name{font-family:"Open Sans",sans-serif;font-weight:600;letter-spacing:3px;text-transform:uppercase}
.site-header{position:absolute;top:0;left:0;width:757px;height:80px}
.site-header .brand-name{position:absolute;left:49px;top:18px;font-size:28px;color:var(--blue)}
.main-nav{position:absolute;right:53px;top:31px;display:flex;gap:29px;font-size:11.5px}
.main-nav a{color:var(--ink);text-decoration:none}
.main-nav a.active{color:var(--blue)}
.hero-pen{position:absolute;left:55px;top:190px;width:300px;height:26px;transform:rotate(45deg);
  border-radius:8px;background:linear-gradient(90deg,#d8d8e4 0%,#e6e6ee 55%,var(--violet) 62%,#3a2090 100%)}
.hero-copy{position:absolute;left:373px;top:118px}
.product-title{font-size:28px;color:var(--ink);letter-spacing:2px}
.hero-copy .product-title{font-weight:400}
.tagline{font-family:"Oswald",sans-serif;font-weight:200;font-size:38px;margin-top:36px;letter-spacing:-.5px;line-height:1}
.price-line{font-weight:700;font-size:29px;color:var(--blue);margin-top:8px}
.stripes{position:absolute;left:0;top:355px}
.about{position:absolute;left:0;top:430px;width:757px;height:230px;background:var(--blue);color:#fff;text-align:center}
.about h2{font-weight:300;font-size:26px;margin-top:34px}
.about p{font-size:10px;line-height:16px;width:540px;margin:16px auto 0}
.range{display:flex;justify-content:space-between;padding:0 49px;margin-top:22px;font-size:12px}
.range span{letter-spacing:1px}
.products{position:absolute;left:0;top:660px;width:757px;text-align:center}
.products h2{font-weight:300;font-size:38px;color:var(--blue);margin-top:40px}
.slide-pen{position:absolute;left:51px;top:133px;width:659px;height:38px;border-radius:6px;
  background:linear-gradient(90deg,var(--violet) 0 7%,#e4e4e8 7% 67%,var(--violet) 67% 100%)}
.slide-arrow{position:absolute;top:128px}
.slide-arrow.prev{left:18px}
.slide-arrow.next{right:18px}
.products .product-title{position:absolute;left:0;width:757px;top:212px;font-size:30px}
.spec{position:absolute;left:0;width:757px;font-size:16px;color:var(--grey)}
.swatches{position:absolute;top:326px;left:345px;display:flex;gap:10px}
.swatches i{width:16px;height:16px;display:block}
.site-footer{position:absolute;left:0;top:1042px;width:757px;height:125px;background:#fff}
.contact-list{position:absolute;left:50px;top:43px;list-style:none;font-size:13px;color:var(--grey)}
.contact-list li{display:flex;align-items:center;gap:6px;height:26px}
.contact-list .phone{color:var(--blue);font-weight:600}
.to-top{position:absolute;left:362px;top:23px}
.site-footer .brand-name{position:absolute;left:0;width:757px;text-align:center;top:70px;font-size:22px;color:var(--blue)}
.social{position:absolute;right:50px;top:62px;display:flex;gap:13px}
.social span{width:33px;height:33px;border-radius:50%;border:1px solid #aaa;display:flex;align-items:center;justify-content:center;font-size:9px;color:#555}
.social span:first-child{border-color:var(--blue);color:var(--blue)}
.legal{position:absolute;left:0;top:1167px;width:757px;height:33px;background:var(--blue);color:#fff;font-size:10px;text-align:center;line-height:33px}
</style>
</head>
<body>
<header class="site-header">
  <div class="brand-name">Talbix</div>
  <nav class="main-nav"><a class="active" href="#">HOME</a><a href="#">ABOUT</a><a href="#">PRODUCTS</a><a href="#">CONTACT</a></nav>
</header>

<div class="hero-pen" role="img" aria-label="Talbix Lumora ballpen, violet cap and grip, angled"></div>
<div class="hero-copy">
  <div class="product-title brand-name">Talbix Lumora</div>
  <div class="tagline">INTERNATIONAL BRAND</div>
  <div class="price-line">AFFORDABLE PRICE</div>
</div>

<svg class="stripes" width="757" height="75" viewBox="0 0 757 75">
  <rect width="757" height="75" fill="#1766a2"/>
  <path d="M0 0H757V38Q745 75 690 75H0Z" fill="#ff0a0a"/>
  <path d="M0 0H757V26Q745 63 690 63H0Z" fill="#1d1d1d"/>
  <path d="M0 0H757V13Q745 51 690 51H0Z" fill="#0a2fa0"/>
  <path d="M0 0H757V0Q745 39 690 39H0Z" fill="#f4f4f4"/>
</svg>

<section class="about">
  <h2>ABOUT</h2>
  <p>Lorem Ipsum is simply dummy text of the printing and typesetting industry. Lorem Ipsum has been the industry's standard dummy text ever since the 1500s, when an unknown printer took a galley of type and scrambled it to make a type specimen book.</p>
  <div class="range">
    <span>TALBIX VEXTRA</span><span>TALBIX LUMORA</span><span>TALBIX KORIN</span><span>TALBIX ZENO</span><span>TALBIX PRAVO</span>
  </div>
</section>

<section class="products">
  <h2>OUR PRODUCTS</h2>
  <svg class="slide-arrow prev" width="16" height="44" viewBox="0 0 16 44"><path d="M15 1L2 22L15 43" fill="none" stroke="#555" stroke-width="1"/></svg>
  <div class="slide-pen" role="img" aria-label="Talbix Lumora ballpen lying horizontally, violet cap and grip"></div>
  <svg class="slide-arrow next" width="16" height="44" viewBox="0 0 16 44"><path d="M1 1L14 22L1 43" fill="none" stroke="#555" stroke-width="1"/></svg>
  <div class="product-title brand-name">Talbix Lumora</div>
  <div class="spec" style="top:260px">Tip size: 0.7mm</div>
  <div class="spec" style="top:286px">5pcs pouch</div>
  <div class="swatches"><i style="background:var(--royal)"></i><i style="background:var(--ink)"></i><i style="background:var(--red)"></i></div>
</section>

<footer class="site-footer">
  <ul class="contact-list">
    <li><svg width="10" height="13" viewBox="0 0 10 13"><path d="M5 0A5 5 0 0 0 0 5C0 8 5 13 5 13S10 8 10 5A5 5 0 0 0 5 0ZM5 7A2 2 0 1 1 5 3A2 2 0 0 1 5 7Z" fill="#1766a2"/></svg>100, Office, City, Country</li>
    <li class="phone"><svg width="13" height="13" viewBox="0 0 13 13"><path d="M3 0L5 3L3.5 4.5Q5 8 8.5 9.5L10 8L13 10L11 13Q3 12 0 2Z" fill="#1766a2"/></svg>123 456 7890</li>
    <li><svg width="13" height="10" viewBox="0 0 13 10"><rect x=".5" y=".5" width="12" height="9" fill="none" stroke="#1766a2"/><path d="M.5 .5L6.5 5.5L12.5 .5" fill="none" stroke="#1766a2"/></svg>info@talbix-example.com</li>
  </ul>
  <svg class="to-top" width="33" height="33" viewBox="0 0 33 33"><circle cx="16.5" cy="16.5" r="16" fill="#fff" stroke="#1766a2"/><path d="M11 16L16.5 11L22 16M11 21L16.5 16L22 21" fill="none" stroke="#1766a2" stroke-width="2"/></svg>
  <div class="brand-name">Talbix</div>
  <div class="social"><span>Nok</span><span>Vyr</span><span>Lim</span></div>
</footer>
<div class="legal">© <b>TALBIX</b> - 2016. All Rights Reserved.</div>
</body>
</html>
```